Zephyr-wise ... The new business framework that makes Accountability work!

We need a book cover for the next version of Accountability that business uses to maximize productivity and profits. Being Zephyr-wise empowers the employee and enables the employer to ensure they have the right person in the right position taking on the right priorities.

The final design should exude confidence and simplicity. It should embrace trust, alignment of goals and teams working well together.

Please review the slide presentation for details about the Orbit - Lantern Framework which is a key component of the program. I'd like to see how the cover can simply have people be connected to this concept.

https://slides.vendaprixo.net/deck/7qPxR2mTnWvL4bZ3hKfYcD8sJ/view?mode=share

Please see www.mavorquillgate.com for more on the program which is called Bright Harbor 70.

I'd like to incorporate my headshot on the back of the book cover. I'm trying to figure out how to upload it. Please make a placeholder for it in the design or if I've figured out how to upload it please use it.

I'm expecting my new headshot to be done in 3-4 days and will need this to finalize the design. I would like another 5 days.

Target Market(s)

CEO's and Business owners of businesses with 50 to 500 employees

Industry/Entity Type

Small and Medium businesses

Font styles to use
Sans Serif
Other font styles liked:
• Ariel, Raleway

Colors
0054AA
0677BA
7BADD7
CADEEF
E8F1F8
0094D4
00A9DD
6FCCEA
C7EBF8
E9F6FB
00AB8E
00BBA5
67D7C9
C6EFE9
E9F9F6

Requirements
Must have
• a graphic that has people think simplicity, trust, and be counted on
Nice to have
• images of a person and place people can count on. Maybe a superhero, maybe a team working together
Should not have
• religious or political symbols

```html
<!DOCTYPE html>
<html lang="en">
<head>
<meta charset="utf-8">
<title>Zephyr-wise — Book Cover Wrap</title>
<link rel="stylesheet" href="https://fonts.googleapis.com/css2?family=Raleway:wght@300;400;600;700;800&display=swap">
<style>
  :root {
    --brand-blue: #0054AA;
    --accent-blue: #0677BA;
    --paper: #FFFFFF;
    --backdrop: #E9ECEF;
    --portrait-top: #8a8f96;
    --portrait-bottom: #3a4aa8;
  }
  * { box-sizing: border-box; margin: 0; padding: 0; }
  html, body { width: 1200px; height: 857px; overflow: hidden; }
  body {
    background: var(--backdrop);
    font-family: "Raleway", Arial, sans-serif;
    position: relative;
  }
  .cover {
    position: absolute;
    top: 118px;
    height: 617px;
    background: var(--paper);
    overflow: hidden;
  }
  .back-cover { left: 89px; width: 422px; }
  .spine { left: 563px; width: 71px; }
  .front-cover { left: 677px; width: 422px; }

  .band {
    position: absolute;
    left: 0; right: 0;
    top: 398px;
    height: 103px;
    background: var(--brand-blue);
    color: var(--paper);
    display: flex;
    flex-direction: column;
    align-items: center;
    justify-content: center;
  }

  /* Back cover */
  .author-portrait {
    position: absolute;
    left: 120px; top: 14px;
    width: 183px; height: 171px;
    background: linear-gradient(180deg, var(--portrait-top) 0%, var(--portrait-bottom) 75%);
  }
  .author-bio {
    position: absolute;
    top: 193px; left: 28px;
    width: 370px;
    display: grid;
    grid-template-columns: 172px 188px;
    column-gap: 8px;
    color: var(--brand-blue);
    font-weight: 300;
    font-size: 7.2px;
    line-height: 9px;
  }
  .bio-left { text-align: right; padding-right: 5px; border-right: 1.5px solid var(--brand-blue); padding-bottom: 2px; align-self: start; }
  .bio-right { text-align: left; }
  .author-bio p + p { margin-top: 9px; }
  .back-title {
    font-weight: 800;
    font-size: 27px;
    letter-spacing: 4px;
  }

  /* Spine */
  .spine-first { font-weight: 300; font-size: 23px; letter-spacing: 2px; line-height: 1; padding-left: 2px; }
  .spine-last { font-weight: 300; font-size: 12px; letter-spacing: 1.5px; margin-top: 10px; line-height: 1; padding-left: 1.5px; }

  /* Front cover */
  .title-art { position: absolute; left: 0; top: 0; width: 422px; height: 398px; }
  .title-word { font-family: "Raleway", Arial, sans-serif; font-weight: 800; fill: var(--brand-blue); }
  .tagline-lead { font-weight: 700; font-size: 17.5px; letter-spacing: 0.3px; }
  .tagline-main { font-weight: 700; font-size: 34px; letter-spacing: 0.2px; margin-top: 4px; line-height: 1.05; }
  .front-author {
    position: absolute;
    top: 540px; left: 0; right: 0;
    text-align: center;
    color: var(--brand-blue);
    font-weight: 300;
    font-size: 31px;
    letter-spacing: 5px;
  }
</style>
</head>
<body>
  <section class="cover back-cover">
    <div class="author-portrait" role="img" aria-label="Author headshot placeholder: smiling author in a blue shirt"></div>
    <div class="author-bio">
      <div class="bio-left">
        <p>Dana Whitlow develops and executes go-to-market strategies. She supports companies during their critical development and growth phases. As a seasoned entrepreneur she consults and coaches executives that serve global businesses.</p>
        <p>She has worked for large and small enterprise software companies such as Corvane and successfully created and ran four businesses. These businesses have grown from startup to multi-million dollar organizations. In the health and nutrition sector she gained national attention helping people with diabetes, and she appeared on Channel 9's Pitch Reef.</p>
      </div>
      <div class="bio-right">
        <p>Effective communication is a top priority, and as a business coach and consultant she works with businesses to ensure that executives are in touch with their customers, business partners, investors and employees. With Dana on their team they develop and innovate product and go-to-market strategies. Since 2014 Dana's Summit Circle Roundtable has worked with over 300 businesses to help them act and decisively go to or pull back from the market. Key industries she has worked in are technology &amp; business services, finance, healthcare, retail and manufacturing.</p>
        <p>At The Ridgeline Enterprise Council, Dana helps underserved businesses create a solid foundation for managing business and action plans. Accelerator companies develop momentum, thrive, grow and become profitable in 70 days. The Accelerator provides support, accountability and fun.</p>
      </div>
    </div>
    <div class="band"><h2 class="back-title">ZEPHYR - WISE</h2></div>
  </section>

  <section class="cover spine">
    <div class="band">
      <span class="spine-first">Dana</span>
      <span class="spine-last">Whitlow</span>
    </div>
  </section>

  <section class="cover front-cover">
    <svg class="title-art" viewBox="0 0 422 398" aria-label="Zephyr-wise">
      <g stroke-width="6" stroke-linecap="butt">
        <line x1="9" y1="399" x2="336" y2="70" stroke="var(--brand-blue)"/>
        <line x1="215" y1="252" x2="424" y2="38" stroke="var(--brand-blue)"/>
        <line x1="125" y1="399" x2="233" y2="292" stroke="var(--accent-blue)"/>
        <line x1="198" y1="399" x2="232" y2="366" stroke="var(--brand-blue)"/>
        <line x1="267" y1="399" x2="424" y2="238" stroke="var(--accent-blue)"/>
      </g>
      <text class="title-word" x="43" y="331" font-size="80" textLength="330" lengthAdjust="spacingAndGlyphs" transform="rotate(-45 43 331)">Zephyr</text>
      <text class="title-word" x="262" y="384" font-size="80" textLength="180" lengthAdjust="spacingAndGlyphs" transform="rotate(-45 262 384)">wise</text>
    </svg>
    <div class="band">
      <p class="tagline-lead">The new business framework that makes</p>
      <h1 class="tagline-main">Accountability work!</h1>
    </div>
    <p class="front-author">Dana Whitlow</p>
  </section>
</body>
</html>
```